Hair salon and Nail salon in Hawaii need a newspaper Ad design.

We need a newspaper Ad design for new open hair & nail salon in Waikiki Hawaii.Our Recommendation service for hair is "Head Spa" $30+tax and for nail is "Manicure Treatment Course" (Filing+Cuticle Care+Massage+Coloring) $20+tax.
We would like to see Hawaiian taste color and also having sense of luxury design. The ad size is W 5.0” x H 6.375”.
I would customers to know the shop place(Lanakila Crest Hotel 1F) , phone(808-555-0173), instagram(salonbrightwave) , our web site https://salonbrightwave.example and recommend services. For Web or Instagram , QR code is acceptable.

Target Market(s)

women & men

Industry/Entity Type

Beauty Salon

Font styles to use
Serif

Colors

Designer to choose colors to be used in the design.

Requirements
Must have
• Tagline for local customers. Shop Name is "SALON BRIGHTWAVE".the shop place(Lanakila Crest Hotel 1F) , phone(808-555-0173), instagram(salonbrightwave) and recommend services.
Nice to have
• Our services are competitive, but we don't want to be seen as just cheap and low quality.

```html
<!DOCTYPE html>
<html lang="en">
<head>
<meta charset="utf-8">
<title>Salon Brightwave – Newspaper Ad</title>
<link rel="stylesheet" href="https://fonts.googleapis.com/css2?family=Montserrat:wght@300;400;600;700&display=swap">
<style>
  :root {
    --red: #c8161b;
    --ink: #2e2e2e;
    --blush: #e8c0b0;
    --paper: #ffffff;
    --page: #ffffff;
  }
  * { box-sizing: border-box; margin: 0; padding: 0; }
  html, body {
    width: 1200px; height: 1200px; overflow: hidden;
    background: var(--page);
    font-family: "Montserrat", sans-serif;
    color: var(--ink);
  }
  .ad {
    position: absolute; left: 107px; top: 214px;
    width: 993px; height: 778px;
    background: var(--paper);
    overflow: hidden;
    box-shadow: 0 0 4px rgba(0,0,0,0.08);
  }
  .ad-shapes { position: absolute; inset: 0; }

  .brand-bar {
    position: absolute; left: 54px; top: 59px;
    display: flex; align-items: center; gap: 25px;
  }
  .brand-square { width: 42px; height: 44px; background: var(--ink); }
  .brand-name {
    font-weight: 300; font-size: 40px; letter-spacing: 1px;
    line-height: 1; color: var(--ink);
  }

  .headline {
    position: absolute; left: 50px; top: 134px;
    font-weight: 700; font-size: 68px; line-height: 64px; letter-spacing: 1px;
  }
  .headline .accent { color: var(--red); display: block; }
  .headline .dark { color: var(--ink); display: block; }

  .service-title {
    position: absolute; left: 54px;
    font-weight: 700; font-size: 23px; line-height: 31px; letter-spacing: 1.2px;
    color: var(--ink);
  }
  .service-title.hair { top: 283px; }
  .service-title.nail { top: 447px; }
  .tag-red {
    background: var(--red); color: #fff; padding: 0 4px;
  }

  .offer-name {
    position: absolute; left: 54px;
    background: var(--blush); color: var(--ink);
    font-weight: 700; letter-spacing: 0.6px;
  }
  .offer-name.hair {
    top: 358px; width: 106px; height: 31px;
    font-size: 15px; line-height: 31px; text-align: center;
  }
  .offer-name.nail {
    top: 524px; width: 300px; height: 38px; padding: 3px 7px 0;
    font-size: 15px; line-height: 18px;
  }
  .offer-name .detail {
    display: block; font-weight: 400; font-size: 11.5px; line-height: 13px; letter-spacing: 0.3px;
  }
  .price {
    position: absolute; background: var(--ink); color: #fff;
    font-weight: 700; font-size: 21px; height: 31px; line-height: 31px;
    text-align: center; letter-spacing: 0.5px;
  }
  .price sup { font-size: 11px; vertical-align: 8px; margin-right: 1px; }
  .price.hair { left: 160px; top: 358px; width: 129px; }
  .price.nail { left: 54px; top: 567px; width: 114px; height: 30px; line-height: 30px; }

  .divider {
    position: absolute; left: 53px; top: 428px; width: 450px; height: 3px;
    background: var(--ink);
  }

  .contact {
    position: absolute; left: 50px; top: 633px;
    list-style: none;
  }
  .contact li {
    display: flex; align-items: center; gap: 8px;
    color: #fff; font-weight: 700; font-size: 16.5px; letter-spacing: 0.4px;
    height: 28px; margin-bottom: 1.5px;
  }
  .contact svg { width: 16px; height: 16px; flex: none; }
  .contact .dot { width: 15px; height: 15px; border-radius: 50%; background: var(--red); flex: none; }
</style>
</head>
<body>
<main class="ad">
  <svg class="ad-shapes" width="993" height="778" viewBox="0 0 993 778" xmlns="http://www.w3.org/2000/svg">
    <defs>
      <linearGradient id="portraitMain" x1="0" y1="0" x2="1" y2="1">
        <stop offset="0" stop-color="#d9b7a2"/>
        <stop offset="0.45" stop-color="#c99d86"/>
        <stop offset="1" stop-color="#6e5446"/>
      </linearGradient>
      <linearGradient id="portraitNail" x1="0" y1="0" x2="1" y2="1">
        <stop offset="0" stop-color="#7a5a46"/>
        <stop offset="0.5" stop-color="#e2c2ae"/>
        <stop offset="1" stop-color="#cfa98f"/>
      </linearGradient>
    </defs>

    <!-- top dark triangle -->
    <polygon points="512,0 822,0 666,154" fill="var(--ink)"/>
    <!-- main portrait -->
    <polygon role="img" aria-label="Photo of a woman with long brown hair and red manicured nails touching her cheek"
             points="452,378 830,0 993,0 993,778 840,778 668,606" fill="url(#portraitMain)"/>
    <!-- top-right red corner -->
    <polygon points="926,0 993,0 993,64" fill="var(--red)" stroke="#fff" stroke-width="6"/>
    <!-- bottom-right dark corner -->
    <polygon points="993,688 993,778 900,778" fill="var(--ink)" stroke="#fff" stroke-width="6"/>
    <!-- bottom dark band -->
    <polygon points="0,616 326,616 490,778 0,778" fill="var(--ink)"/>
    <!-- nail portrait diamond -->
    <polygon role="img" aria-label="Photo of a woman with wavy hair showing red nail polish"
             points="326,600 502,431 670,598 496,778" fill="url(#portraitNail)" stroke="#fff" stroke-width="5"/>
    <!-- red bottom triangle -->
    <polygon points="499,778 668,606 840,778" fill="var(--red)" stroke="#fff" stroke-width="6"/>
  </svg>

  <header class="brand-bar">
    <span class="brand-square"></span>
    <span class="brand-name">SALON BRIGHTWAVE</span>
  </header>

  <h1 class="headline">
    <span class="accent">SALON</span>
    <span class="dark">BRIGHTWAVE</span>
  </h1>

  <h2 class="service-title hair">OUR RECOMMENDATION<br>SERVICE FOR <span class="tag-red">HAIR</span></h2>
  <div class="offer-name hair">HEAD SPA</div>
  <div class="price hair"><sup>$</sup>30+TAX</div>

  <div class="divider"></div>

  <h2 class="service-title nail">OUR RECOMMENDATION<br>SERVICE FOR <span class="tag-red">NAIL</span></h2>
  <div class="offer-name nail">MANICURE TREATMENT COURSE
    <span class="detail">(Filing+Cuticle Care+Massage+Coloring)</span></div>
  <div class="price nail"><sup>$</sup>20+TAX</div>

  <ul class="contact">
    <li>
      <svg viewBox="0 0 24 24"><path fill="var(--red)" d="M6.6 10.8a15 15 0 0 0 6.6 6.6l2.2-2.2a1 1 0 0 1 1-.25 11.4 11.4 0 0 0 3.6.57 1 1 0 0 1 1 1V20a1 1 0 0 1-1 1A17 17 0 0 1 3 4a1 1 0 0 1 1-1h3.5a1 1 0 0 1 1 1c0 1.25.2 2.45.57 3.57a1 1 0 0 1-.25 1z"/></svg>
      808-555-0173
    </li>
    <li>
      <svg viewBox="0 0 24 24"><path fill="var(--red)" d="M12 2a7 7 0 0 0-7 7c0 5.2 7 13 7 13s7-7.8 7-13a7 7 0 0 0-7-7zm0 9.5A2.5 2.5 0 1 1 12 6.5a2.5 2.5 0 0 1 0 5z"/></svg>
      Lanakila Crest Hotel 1F
    </li>
    <li>
      <svg viewBox="0 0 24 24" fill="none" stroke="var(--red)" stroke-width="2"><circle cx="12" cy="12" r="9"/><path d="M3 12h18M12 3c3 3 3 15 0 18M12 3c-3 3-3 15 0 18"/></svg>
      salonbrightwave.example
    </li>
    <li>
      <span class="dot"></span>
      @salonbrightwave
    </li>
  </ul>
</main>
</body>
</html>
```